Quill And Ferry Business Card

I need a business card designed around my logo (which was designed here on Sketch Forum!)

Target Market(s)

Professional Businesses

Industry/Entity Type

Business

Requirements
Must have
• Details that must be on the business card:

Renata Ovalle
Director
0491 253 608
renata@quillandferry.com.au
www.quillandferry.com.au
PO Box 4720 Marrenby North Tas 7391

```html
<!DOCTYPE html>
<html lang="en">
<head>
<meta charset="utf-8">
<title>Quill And Ferry – Business Card</title>
<link rel="stylesheet" href="https://fonts.googleapis.com/css2?family=Cinzel:wght@500&family=Crimson+Pro:wght@400&family=Open+Sans:wght@400&display=swap">
<style>
  :root {
    --brand-red: #d10000;
    --card-white: #ffffff;
    --ink: #1b1b1b;
    --soft-pink: #f4b9b9;
    --contact-text: #ffe3e3;
    --backdrop: #e9e6e2;
  }
  html, body {
    margin: 0;
    padding: 0;
    width: 1200px;
    height: 1000px;
    overflow: hidden;
    background: var(--backdrop);
  }
  .canvas {
    position: relative;
    width: 1200px;
    height: 1000px;
  }
  .card {
    position: absolute;
    left: 240px;
    width: 720px;
    height: 412px;
    border-radius: 30px;
    overflow: hidden;
    box-shadow: 0 4px 14px rgba(0,0,0,0.18);
    background: var(--brand-red);
  }
  .card--front { top: 62px; }
  .card--back { top: 526px; }

  /* Front */
  .front__white {
    position: absolute;
    left: 0; top: 0; bottom: 0;
    width: 262px;
    background: var(--card-white);
  }
  .front__brand {
    position: absolute;
    left: 30px;
    top: 92px;
    margin: 0;
    font-family: "Cinzel", serif;
    font-weight: 500;
    font-size: 58px;
    letter-spacing: 1px;
    color: var(--ink);
    white-space: nowrap;
    line-height: 1;
  }
  .front__mark {
    position: absolute;
    left: 86px;
    top: 222px;
    width: 118px;
    height: 118px;
    border-radius: 50%;
    background: var(--brand-red);
  }
  .contacts {
    position: absolute;
    right: 34px;
    bottom: 56px;
    margin: 0;
    padding: 0;
    list-style: none;
    font-family: "Open Sans", sans-serif;
    font-size: 19px;
    color: var(--contact-text);
    text-align: right;
  }
  .contacts li {
    display: flex;
    justify-content: flex-end;
    align-items: center;
    gap: 12px;
    line-height: 31px;
    white-space: nowrap;
  }
  .contacts svg {
    width: 16px;
    height: 16px;
    flex: none;
  }

  /* Back */
  .back__white {
    position: absolute;
    right: 0; top: 0; bottom: 0;
    width: 190px;
    background: var(--card-white);
  }
  .back__lockup {
    position: absolute;
    left: 58px;
    top: 104px;
    display: flex;
    align-items: center;
    gap: 16px;
  }
  .back__dot {
    width: 46px;
    height: 46px;
    border-radius: 50%;
    background: var(--soft-pink);
  }
  .back__brand {
    margin: 0;
    font-family: "Cinzel", serif;
    font-weight: 500;
    font-size: 34px;
    color: var(--soft-pink);
    white-space: nowrap;
    line-height: 1;
  }
  .person {
    position: absolute;
    left: 0;
    width: 530px;
    top: 206px;
    text-align center;
    text-align: center;
    font-family: "Crimson Pro", serif;
    color: var(--soft-pink);
  }
  .person__name {
    margin: 0;
    font-size: 40px;
    font-weight: 400;
    line-height: 1.1;
  }
  .person__role {
    margin: 4px 0 0;
    font-size: 22px;
  }
</style>
</head>
<body>
<main class="canvas">

  <section class="card card--front" aria-label="Card front">
    <div class="front__white"></div>
    <h1 class="front__brand">QUILL AND FERRY</h1>
    <div class="front__mark" aria-hidden="true"></div>
    <ul class="contacts">
      <li>0491 253 608
        <svg viewBox="0 0 16 16" aria-hidden="true"><rect x="4" y="1" width="8" height="14" rx="1.5" fill="none" stroke="#1b1b1b" stroke-width="1.4"/><rect x="6" y="12" width="4" height="1.2" fill="#1b1b1b"/></svg>
      </li>
      <li>renata@quillandferry.com.au
        <svg viewBox="0 0 16 16" aria-hidden="true"><rect x="1" y="3" width="14" height="10" rx="1" fill="#ffffff"/><path d="M1.5 3.5 L8 9 L14.5 3.5" fill="none" stroke="#d10000" stroke-width="1.4"/></svg>
      </li>
      <li>www.quillandferry.com.au
        <svg viewBox="0 0 16 16" aria-hidden="true"><g fill="none" stroke="#1b1b1b" stroke-width="1.2"><circle cx="8" cy="8" r="6.5"/><ellipse cx="8" cy="8" rx="2.8" ry="6.5"/><path d="M1.5 8 H14.5 M2.6 4.6 H13.4 M2.6 11.4 H13.4"/></g></svg>
      </li>
      <li>PO Box 4720 Marrenby North Tas 7391
        <svg viewBox="0 0 16 16" aria-hidden="true"><rect x="1" y="3.5" width="14" height="9" rx="1" fill="#f2b233"/><path d="M1.5 4 L8 8.5 L14.5 4" fill="none" stroke="#c98a10" stroke-width="1"/></svg>
      </li>
    </ul>
  </section>

  <section class="card card--back" aria-label="Card back">
    <div class="back__white"></div>
    <div class="back__lockup">
      <div class="back__dot" aria-hidden="true"></div>
      <p class="back__brand">QUILL AND FERRY</p>
    </div>
    <div class="person">
      <p class="person__name">Renata Ovalle</p>
      <p class="person__role">Director</p>
    </div>
  </section>

</main>
</body>
</html>
```